GUARANTEED 4 sample word cards for inclusive primary education (the swan, the icebear, the cat, sad)

in short: it's about drawing a swan, at icebear, a cat, a sad person (male / female) and arranging them on word cards with some additional information As there which only one design submitted, Which was missing the point I Decided to translate everything myself and upload it again. Requirements Within an open educational ressources (OER) project, materials for the interest-based spelling workout are to be created. In the preparation of this project four example sample word cards are to be developed. Later They Should be compiled dynamically from a database. Since the needs of the teachers are very different, it would be advantageous to integrate the different design elements as layers in Photoshop so did one can show how diverse the cards can look later by hiding / showing the layers. The materials shoulderstand be distributed under cc-0 license. It is about 4 sample cards (the swan, the icebear, the cat, sad), Which shoulderstand demonstrate how search cards can look. German: As part of an OER project are materials to interest-based spelling learning occur. In the preparation of the project (to be created also a permanent position for a / n Designer / -in under which) are four examplarische Sample word cards are developed. Later this should be assembled dynamically from a database. Since the needs of teachers / -Innen are very different, it would be desirable to integrate the various design elements as layers in Photoshop, so you can show how diverse can look the cards later. The materials are to be distributed under cc-0 license. It is about 4 example cards that demonstrate how can such cards look. The most expensive part is undoubtedly the drawings (polar bear, swan, cat and sad child / sad person). Common elements - speech symbol Lindqvist (see http: //media.brenzo-haus. de / media / catalog / product / cache / 4 / image / 3ab41cde77280f19e4c2da6b58190a42 / 0/7 / 07216_1.jpg) - underline articles colored or colored or point mark (male - red, male - blue, neuter - green) - writing of definition and article (once https://typevault.example/en/font/grundschrift and once a school Ausgangsschrift eg https://www.vorlind.example/pulse/Tavrel/de_DE.CMS.displayCMS.209797./die-schulausgangsschrift -sas-free-download-vorlind) - Ruling based on http://www.t-wellbrig.example/wp-content/uploads/2010/01/Heft-006-innen.png (and even without house) - picture on the right side - pictures with people, each as a girl / boy, different skin colors (or all as layers in Photoshop, where I can hide it myself) - syllable sheets (instead of the | http://tryclassmill.example/wp- content / uploads / 2015_2_Silbenboegen_Kombo.png) - colored syllables (blue and red) - stem color (red), ending black - cases if necessary on the back of the card - Format Din A7, rounded corners images should as svg / or levels exist (different skin color / hair color / gender) drawings should stylized and not be too childish and love of detail, so that they are attractive to adults (and as can be used in work with fugitives). You should also black / white and be usable with red / green blindness. The exact requirements are in the description file. For any questions please contact via the platform or paulr.hessling@hs-tarnow.example Ps: If a logo for (spelling) learning, including drops, it is also nich bad;) If you interested in a long-term employment in a project have the university, we appreciate if you mention this.
Target Market(s)
pupils in primary school, so but older students and adults (for example refugees who started to learn the language) students / -Innen primary school (until fourth grade) as well as older adolescents / adults, therefore, not to child pictures
Industry/Entity Type
Education
Font styles to use
Other font styles liked:
- see additional file

Requirements
Must have
- psd files with levels, to show and hide different elements self drawn images, Which Could be released under a CC-0 license. see additional file for more info and sample German: .psd files with labeled layers, in which the individual elements can be hidden. Self-drawn graphics which can then be released under cc-0 Stock

```html
<!DOCTYPE html>
<html lang="de">
<head>
<meta charset="utf-8">
<title>Wortkarte – der Eisbär</title>
<link rel="stylesheet" href="https://fonts.googleapis.com/css2?family=Andika&display=swap">
<style>
  :root {
    --page: #ffffff;
    --frame: #bfc1c0;
    --shadow: #4a4a4a;
    --card: #ffffff;
    --ink: #1a1a1a;
    --ink-soft: #6a6a6a;
    --masc: #1a9ad6;
    --row-shade: #dcdddd;
    --picture-tone: #eef0f1;
  }
  html, body {
    margin: 0; padding: 0;
    width: 927px; height: 1200px;
    overflow: hidden;
    background: var(--page);
  }
  body {
    position: relative;
    font-family: "Andika", sans-serif;
    color: var(--ink);
  }
  .word-card {
    position: absolute;
    left: 161px;
    width: 635px;
    height: 451px;
    background: var(--frame);
    box-shadow: 8px 7px 4px var(--shadow);
  }
  .word-card--front { top: 98px; }
  .word-card--back  { top: 611px; }
  .card-face {
    position: absolute;
    left: 11px; top: 12px;
    width: 611px; height: 424px;
    background: var(--card);
    border-radius: 17px;
  }
  .article-house {
    position: absolute;
    left: 38px; top: 33px;
  }
  .headword {
    position: absolute;
    margin: 0;
    font-weight: 400;
    font-size: 42px;
    line-height: 1;
    white-space: nowrap;
  }
  .headword--singular { left: 94px; top: 88px; }
  .headword--plural   { left: 73px; top: 160px; }
  .article--masc { color: var(--masc); }
  .picture-frame {
    position: absolute;
    left: 317px; top: 32px;
    width: 280px; height: 232px;
    border: 2px solid var(--ink);
    border-radius: 18px;
    background: linear-gradient(180deg, #ffffff 0%, var(--picture-tone) 100%);
  }
  .example-sentence {
    position: absolute;
    left: 38px; top: 236px;
    margin: 0;
    font-size: 18px;
    color: #333;
  }
  .word-field {
    position: absolute;
    left: 38px; top: 290px;
    margin: 0;
    font-size: 18px;
    color: #333;
    word-spacing: 2px;
  }
  .word-type {
    position: absolute;
    left: 114px; top: 335px;
    display: flex;
    align-items: flex-end;
    gap: 9px;
  }
  .word-type__label {
    font-size: 38px;
    line-height: 1;
    padding-bottom: 12px;
  }
  .case-table {
    position: absolute;
    left: 16px; top: 92px;
    width: 582px;
    font-size: 18.5px;
  }
  .case-table__head {
    position: absolute;
    left: 266px; top: 0;
    width: 330px; height: 44px;
    border: 1.5px solid var(--ink);
    border-bottom: none;
    border-radius: 12px 12px 0 0;
  }
  .case-table__body {
    position: absolute;
    left: 0; top: 45px;
    width: 596px; height: 166px;
    border: 1.5px solid var(--ink);
    border-top: none;
    border-radius: 0 0 12px 12px;
    overflow: hidden;
  }
  .case-row {
    position: absolute;
    left: 0; width: 100%;
    height: 41px;
  }
  .case-row--shaded { background: var(--row-shade); }
  .case-row span, .case-table__head span {
    position: absolute;
    top: 50%;
    transform: translateY(-50%);
    white-space: nowrap;
  }
  .case-name { left: 9px; }
  .case-form { color: var(--ink-soft); }
  .case-form--sg { left: 283px; }
  .case-form--pl { left: 459px; }
  .col-title--sg { left: 27px; }
  .col-title--pl { left: 228px; }
  .back-outline {
    position: absolute;
    left: 16px; top: 92px;
  }
</style>
</head>
<body>

<section class="word-card word-card--front">
  <div class="card-face">
    <svg class="article-house" width="48" height="98" viewBox="0 0 48 98" aria-hidden="true">
      <polygon points="24,0 47,33 1,33" fill="var(--masc)"/>
      <rect x="12" y="33" width="26" height="64" fill="none" stroke="var(--ink)" stroke-width="1.5"/>
      <line x1="12" y1="55" x2="38" y2="55" stroke="var(--ink)" stroke-width="1.5"/>
      <line x1="12" y1="76" x2="38" y2="76" stroke="var(--ink)" stroke-width="1.5"/>
    </svg>

    <h1 class="headword headword--singular"><span class="article--masc">der</span> Eisbär</h1>
    <p class="headword headword--plural">die Eisbären</p>

    <div class="picture-frame" role="img" aria-label="Zeichnung eines Eisbären auf dem Eis vor verschneiten Tannen"></div>

    <p class="example-sentence">Der Eisbär frisst den Fisch.</p>
    <p class="word-field">Tier | groß | weiß | Säugetier | Bär | Arktis</p>

    <div class="word-type">
      <svg width="66" height="67" viewBox="0 0 66 67" aria-hidden="true">
        <polygon points="33,0 66,67 0,67" fill="var(--ink)"/>
      </svg>
      <span class="word-type__label">Substantiv / Nomen</span>
    </div>
  </div>
</section>

<section class="word-card word-card--back">
  <div class="card-face">
    <div class="case-table" role="table" aria-label="Deklination von der Eisbär">
      <div class="case-table__head" role="row">
        <span class="col-title--sg" role="columnheader">Singular</span>
        <span class="col-title--pl" role="columnheader">Plural</span>
      </div>
      <div class="case-table__body">
        <div class="case-row case-row--shaded" style="top:0" role="row">
          <span class="case-name">Nominativ (wer?/was?)</span>
          <span class="case-form case-form--sg">der Eisbär</span>
          <span class="case-form case-form--pl">die Eisbären</span>
        </div>
        <div class="case-row" style="top:41px" role="row">
          <span class="case-name">Genitiv (wessen?)</span>
          <span class="case-form case-form--sg">des Eisbären</span>
          <span class="case-form case-form--pl">der Eisbären</span>
        </div>
        <div class="case-row case-row--shaded" style="top:82px" role="row">
          <span class="case-name">Dativ (wem?)</span>
          <span class="case-form case-form--sg">dem Eisbären</span>
          <span class="case-form case-form--pl">den Eisbären</span>
        </div>
        <div class="case-row" style="top:123px" role="row">
          <span class="case-name">Akkusativ (wen?/was?)</span>
          <span class="case-form case-form--sg">den Eisbären</span>
          <span class="case-form case-form--pl">die Eisbären</span>
        </div>
      </div>
    </div>
    <svg class="back-outline" width="598" height="214" viewBox="0 0 598 214" aria-hidden="true">
      <path d="M0.75,58 Q0.75,45.5 13,45.5 L266,45.5" fill="none" stroke="var(--ink)" stroke-width="1.5"/>
    </svg>
  </div>
</section>

</body>
</html>
```